General Contractors need a new Crisp updated Card Design

We need a new business card design for our company of 25 years based in Toronto call Holvaster Building Inc. : Our goal is to be the leading commercial contractors in Toronto by providing exceptional value to our clients. We work very hard to deliver professional, quality, service in conjunction with consistent price competitiveness to all of our clients on every single project.

Target Market(s)

Design & Build Clients

Industry/Entity Type

Construction Company

Contact Information for Business Card

Address:
18 North Tamlin Glen Road, Unit 57, Marbrook Vale, ON, K7T 2R9
Office: 905-218-5937

Holvasters Logo
Employee Job Description
Employee Cell Phone #
Employee Email
www.holvaster-example.com

Colors

Designer to choose colors to be used in the design.

Requirements
Must have
• Quote Company Saying:
• "Professional. Quality. Service."
Nice to have
• New Crisp up to date look. simple & fresh ( Not to Busy)
Should not have
• NO BLUE PRINTS ON THE BUSINESS CARDS

```html
<!DOCTYPE html>
<html lang="en">
<head>
<meta charset="utf-8">
<title>Holvaster Building Inc. – Business Card</title>
<link rel="stylesheet" href="https://fonts.googleapis.com/css2?family=PT+Serif:wght@400;700&display=swap">
<style>
  :root {
    --page-bg: #e4e4e4;
    --brand-green: #0b6556;
    --brand-green-dark: #085246;
    --sage: #a9b9ae;
    --card-white: #f7f7f5;
    --text-light: #ffffff;
    --text-soft: #d8e8e3;
  }
  * { box-sizing: border-box; margin: 0; padding: 0; }
  html, body {
    width: 1200px; height: 852px; overflow: hidden;
    background: var(--page-bg);
    font-family: "PT Serif", Georgia, serif;
  }
  .canvas {
    position: relative; width: 1200px; height: 852px;
    display: flex; flex-direction: column; align-items: center; justify-content: center; gap: 48px;
  }
  .card {
    position: relative; width: 560px; height: 320px; border-radius: 22px; overflow: hidden;
    box-shadow: 0 6px 18px rgba(0,0,0,0.18);
  }
  /* Front */
  .card-front { background: var(--brand-green); color: var(--text-light); }
  .front-brand {
    position: absolute; left: 0; right: 0; top: 112px;
    display: flex; align-items: center; justify-content: center; gap: 16px;
  }
  .brand-square { width: 44px; height: 44px; background: var(--text-light); flex: none; }
  .front-brand .brand-text { display: flex; flex-direction: column; gap: 6px; }
  .front-brand .brand-name { font-size: 32px; font-weight: 700; letter-spacing: 0.5px; line-height: 1.1; }
  .slogan { font-size: 12px; letter-spacing: 3px; text-transform: uppercase; }
  .front-web {
    position: absolute; left: 0; right: 0; bottom: 34px;
    display: flex; align-items: center; justify-content: center; gap: 14px;
    font-size: 14px; letter-spacing: 1px;
  }
  .front-web .rule { width: 70px; height: 2px; background: var(--text-light); opacity: 0.8; }

  /* Back */
  .card-back { background: var(--brand-green); }
  .back-shape { position: absolute; inset: 0; }
  .back-brand {
    position: absolute; left: 24px; top: 92px; width: 190px;
    display: flex; flex-direction: column; align-items: center; gap: 12px;
    color: var(--brand-green);
  }
  .back-brand .brand-square { width: 64px; height: 64px; background: var(--brand-green); }
  .back-brand .brand-name { font-size: 22px; font-weight: 700; text-align: center; line-height: 1.15; }
  .contact {
    position: absolute; left: 326px; top: 58px; color: var(--text-light);
  }
  .contact-name { font-size: 22px; font-weight: 700; }
  .contact-title { font-size: 13px; color: var(--text-soft); margin-top: 2px; margin-bottom: 16px; }
  .contact-list { list-style: none; font-size: 13px; line-height: 1.55; }
  .contact-list li { display: flex; align-items: center; gap: 8px; }
  .contact-list svg { width: 12px; height: 12px; flex: none; fill: var(--text-light); }
  .contact-address { font-size: 13px; line-height: 1.45; margin-top: 14px; }
</style>
</head>
<body>
<main class="canvas">
  <section class="card card-front">
    <div class="front-brand">
      <span class="brand-square"></span>
      <div class="brand-text">
        <span class="brand-name">Holvaster Building Inc.</span>
        <span class="slogan">Professional. Quality. Service.</span>
      </div>
    </div>
    <div class="front-web">
      <span class="rule"></span>
      <span>www.holvaster-example.com</span>
      <span class="rule"></span>
    </div>
  </section>

  <section class="card card-back">
    <svg class="back-shape" viewBox="0 0 560 320" width="560" height="320">
      <path d="M0 0 H276 C220 90 236 230 312 320 H0 Z" fill="var(--sage)"/>
      <path d="M0 0 H262 C204 90 220 230 294 320 H0 Z" fill="var(--card-white)"/>
    </svg>
    <div class="back-brand">
      <span class="brand-square"></span>
      <span class="brand-name">Holvaster<br>Building Inc.</span>
    </div>
    <div class="contact">
      <p class="contact-name">Darren Mosley</p>
      <p class="contact-title">Managing Director</p>
      <ul class="contact-list">
        <li><svg viewBox="0 0 12 12"><rect x="3" y="0.5" width="6" height="11" rx="1.2"/></svg>416-730-2894</li>
        <li><svg viewBox="0 0 12 12"><path d="M1 4 Q6 0 11 4 L9.5 5.5 L8 4.5 L4 4.5 L2.5 5.5 Z M3 6 H9 L10 11 H2 Z"/></svg>905-218-5937</li>
        <li><svg viewBox="0 0 12 12"><path d="M0.5 2.5 H11.5 V9.5 H0.5 Z M0.5 2.5 L6 7 L11.5 2.5" stroke="var(--brand-green)" stroke-width="0.8"/></svg>darren.m@holvaster-example.com</li>
        <li><svg viewBox="0 0 12 12"><circle cx="6" cy="6" r="5.5"/></svg>www.holvaster-example.com</li>
      </ul>
      <p class="contact-address">18 North Tamlin Glen Road, Unit 57<br>Marbrook Vale, ON, K7T 2R9</p>
    </div>
  </section>
</main>
</body>
</html>
```